Luminously Grounded Vitality

We want to design a business card that is modern and appealing for an innovative psychedelic telemedicine company that provides at-home ketamine-assisted therapy along with wellness, longevity, and anti-aging medicines. We want to use our deep purple and white plus other colors you can find on our website. We don't have any strict brand guidelines yet so feel free to get creative. We want a very professional, but technology first modern design that will instill trust, peace, calm, but also be attractive to investors in the healthcare and SaaS space.

```html
<!DOCTYPE html>
<html lang="en">
<head>
<meta charset="utf-8">
<title>Luminously Grounded Vitality – Business Card</title>
<link rel="stylesheet" href="https://fonts.googleapis.com/css2?family=Alegreya+Sans:wght@400&family=Libre+Baskerville:wght@700&family=Didact+Gothic&display=swap">
<style>
  :root {
    --backdrop: #e5e5e5;
    --card-white: #ffffff;
    --brand-purple: #876ba8;
    --wordmark-pink: #b574a8;
    --mark-light: #e2e2e2;
    --ink: #3a3a3a;
    --rule: #3a3a3a;
  }
  * { margin: 0; padding: 0; box-sizing: border-box; }
  html, body {
    width: 1033px; height: 1200px; overflow: hidden;
    background: var(--backdrop);
  }
  .canvas { position: relative; width: 1033px; height: 1200px; }

  .card { position: absolute; width: 660px; height: 396px; }
  .card--front { left: 203px; top: 204px; background: var(--card-white); }
  .card--back { left: 193px; top: 637px; background: var(--brand-purple); }

  /* front: brand block */
  .brand {
    position: absolute; left: 0; top: 0; width: 327px; height: 396px;
    display: flex; flex-direction: column; align-items: center; justify-content: center;
    gap: 18px;
  }
  .brand__dot { width: 44px; height: 44px; border-radius: 50%; background: var(--brand-purple); }
  .brand__name {
    font-family: "Alegreya Sans", sans-serif; font-weight: 400;
    font-size: 27px; line-height: 1.1; text-align: center;
    color: var(--wordmark-pink);
  }

  .divider {
    position: absolute; left: 326px; top: 93px; width: 1.5px; height: 211px;
    background: var(--rule);
  }

  /* front: person + contact */
  .person { position: absolute; left: 376px; top: 96px; }
  .person__name {
    font-family: "Libre Baskerville", serif; font-weight: 700;
    font-size: 20px; letter-spacing: 0.2px; color: var(--brand-purple);
  }
  .person__role {
    margin-top: 6px;
    font-family: "Didact Gothic", sans-serif; font-size: 14px;
    letter-spacing: 0.6px; color: var(--ink);
  }

  .contact { position: absolute; left: 351px; top: 192px; list-style: none; }
  .contact__item {
    display: flex; align-items: center; height: 34px;
    font-family: "Didact Gothic", sans-serif; font-size: 16px; color: var(--ink);
  }
  .contact__icon { width: 22px; height: 26px; margin-right: 16px; flex: none; }

  /* back */
  .back__inner {
    position: absolute; inset: 0;
    display: flex; flex-direction: column; align-items: center;
  }
  .back__dot {
    margin-top: 72px; width: 64px; height: 64px; border-radius: 50%;
    background: var(--mark-light);
  }
  .back__name {
    margin-top: 40px;
    font-family: "Alegreya Sans", sans-serif; font-weight: 400;
    font-size: 34px; color: var(--card-white);
  }
  .back__rule { margin-top: 50px; width: 39px; height: 2px; background: var(--card-white); }
  .back__url {
    margin-top: 16px;
    font-family: "Didact Gothic", sans-serif; font-size: 15px;
    letter-spacing: 0.4px; color: var(--card-white);
  }
</style>
</head>
<body>
<main class="canvas">

  <section class="card card--front">
    <div class="brand">
      <span class="brand__dot"></span>
      <p class="brand__name">Luminously Grounded<br>Vitality</p>
    </div>

    <span class="divider"></span>

    <div class="person">
      <h1 class="person__name">DANAWHITFIELD</h1>
      <p class="person__role">CREATIVE DESINGER</p>
    </div>

    <ul class="contact">
      <li class="contact__item">
        <svg class="contact__icon" viewBox="0 0 22 26" aria-hidden="true">
          <rect x="3" y="1" width="16" height="24" rx="1.5" fill="none" stroke="#876ba8" stroke-width="1.2"/>
          <line x1="3" y1="5" x2="19" y2="5" stroke="#876ba8" stroke-width="1"/>
          <line x1="3" y1="21" x2="19" y2="21" stroke="#876ba8" stroke-width="1"/>
          <line x1="9" y1="23" x2="13" y2="23" stroke="#876ba8" stroke-width="1"/>
        </svg>
        014 . 382. 5096
      </li>
      <li class="contact__item">
        <svg class="contact__icon" viewBox="0 0 22 26" aria-hidden="true">
          <circle cx="11" cy="13" r="9.5" fill="none" stroke="#876ba8" stroke-width="1.2"/>
          <circle cx="11" cy="13" r="4" fill="none" stroke="#876ba8" stroke-width="1.2"/>
          <path d="M15 9 v6 q0 2.5 2.5 1.5" fill="none" stroke="#876ba8" stroke-width="1.2"/>
        </svg>
        hello@lgvitality.com
      </li>
      <li class="contact__item">
        <svg class="contact__icon" viewBox="0 0 22 26" aria-hidden="true">
          <path d="M11 24 C5 17 2 13 2 10 a9 9 0 0 1 18 0 c0 3 -3 7 -9 14z" fill="none" stroke="#876ba8" stroke-width="1.2"/>
          <circle cx="11" cy="10" r="3.5" fill="none" stroke="#876ba8" stroke-width="1.2"/>
        </svg>
        18 Larkspur Lane
      </li>
    </ul>
  </section>

  <section class="card card--back">
    <div class="back__inner">
      <span class="back__dot"></span>
      <p class="back__name">Luminously Grounded Vitality</p>
      <span class="back__rule"></span>
      <p class="back__url">www.lgvitality.com</p>
    </div>
  </section>

</main>
</body>
</html>
```